Rehearsal studio business card design needed

My rehearsal studio i bought not that long ago was opened as a hobby originally and was definitely not taken seriously. I am trying to make the new look studio be launched with the new look business cards. I am looking for very simple and clean look cards to match the simple and clean studios. the colour scheme is red and grey. over all i am really just looking for a very simple card that is not too busy and just gets the point accross.
Target Market(s)
Targeting bands, music teachers, students, etc.
Industry/Entity Type
Business
Contact Information for Business Card
Bayridge Sound Centre
Rehearsal and Recording Facilities
Owen Barlow CEO
unit 8, 47 Garvin Road Tallow NSW 2093
0491 382 905
bayridgesoundcentre@mailvex.com
Requirements
Must have
- simplicity
Nice to have

```html
<!DOCTYPE html>
<html lang="en">
<head>
<meta charset="utf-8">
<title>Bayridge Sound Centre – Business Card</title>
<link href="https://fonts.googleapis.com/css2?family=Jost:wght@400;700&display=swap" rel="stylesheet">
<style>
  :root {
    --backdrop: #3a3a3c;
    --card-light: #e9e9e9;
    --card-dark: #2a2a2b;
    --ink: #1c1c1c;
    --brand-red: #b3202a;
    --soft-grey: #9a9a9a;
    --pale: #e4e4e4;
  }
  * { margin: 0; padding: 0; box-sizing: border-box; }
  html, body {
    width: 1200px; height: 900px; overflow: hidden;
    background: var(--backdrop);
    font-family: "Jost", "Century Gothic", sans-serif;
  }
  .sheet {
    width: 1200px; height: 900px;
    display: flex; flex-direction: column;
    align-items: center; justify-content: center; gap: 40px;
  }
  .card {
    position: relative;
    width: 600px; height: 343px;
    border-radius: 3px;
    box-shadow: 0 10px 24px rgba(0,0,0,0.35);
  }
  .card--front { background: var(--card-light); color: var(--ink); }
  .card--back { background: var(--card-dark); }

  .brand {
    position: absolute; left: 175px; top: 62px;
    display: flex; align-items: center; gap: 14px;
  }
  .brand__dot {
    width: 40px; height: 40px; border-radius: 50%;
    background: var(--brand-red); flex: none;
  }
  .brand__name {
    font-size: 33px; font-weight: 700; letter-spacing: -0.5px;
    color: var(--ink); text-transform: lowercase; white-space: nowrap;
  }
  .tagline {
    position: absolute; left: 230px; top: 122px;
    font-size: 20px; color: var(--brand-red); white-space: nowrap;
  }
  .person { position: absolute; left: 48px; top: 188px; }
  .person__name { font-size: 15px; font-weight: 700; letter-spacing: 0.5px; text-transform: uppercase; }
  .person__role { font-size: 13px; }
  .contact {
    position: absolute; left: 118px; top: 240px;
    font-size: 13px; line-height: 1.6;
  }
  .contact__label { color: var(--brand-red); font-weight: 700; }

  .back-brand {
    position: absolute; inset: 0;
    display: flex; flex-direction: column; align-items: center; justify-content: center; gap: 18px;
  }
  .back-brand__dot {
    width: 130px; height: 130px; border-radius: 50%;
    background: var(--brand-red);
  }
  .back-brand__name {
    font-size: 26px; font-weight: 400; color: var(--pale);
    text-transform: lowercase; letter-spacing: 1px;
  }
</style>
</head>
<body>
<main class="sheet">
  <section class="card card--front" aria-label="Business card front">
    <div class="brand">
      <span class="brand__dot"></span>
      <span class="brand__name">Bayridge Sound Centre</span>
    </div>
    <p class="tagline">Rehearsal and Recording Facilities</p>
    <div class="person">
      <p class="person__name">Owen Barlow</p>
      <p class="person__role">CEO</p>
    </div>
    <div class="contact">
      <p>Unit 8, 47 Garvin Road Tallow, NSW 2093 0491 382 905</p>
      <p><span class="contact__label">Email:</span> bayridgesoundcentre@mailvex.com</p>
    </div>
  </section>

  <section class="card card--back" aria-label="Business card back">
    <div class="back-brand">
      <span class="back-brand__dot"></span>
      <span class="back-brand__name">Bayridge Sound Centre</span>
    </div>
  </section>
</main>
</body>
</html>
```